Etiketten für Honig
Wir können es nicht in Worte fassen wie dankbar wir sind mit unserem Einzigartigen Design was uns Wenda die Designerin entworfen hat und unserem schönen spitzen Logo - einfach einmalig. Haben bei beiden Projekten wo Wenda mitgewirkt hat Sie als Gewinnerin ???? gekrönt Umsetzung - Geschmack - Talent Sie setzt alles so schnell um - unkompliziert und denkt selber mit, in allen Punkten wo man selber übersieht Wenda ist sehr zu empfehlen der nach etwas besonders auf der Suche ist. Danke Wenda mehr als Danke ????
Aufgabenstellung
Hallo Ihr lieben
Produktetiketten
Vorderseite
-Markenlogo ist derzeit auch bei Entwurfsplatz in Bearbeitung - mit einem Preisgeld
TERAMILO Spain
-100% Artisan Naturbelassen
Honig aus Andalusien
Sortenamen - zuerst auf Deutsch dann spanisch noch
100% Origen España
Sehr wichtig
Miel de Flores
- Berg Honig
- Miel de Monte -
- Eucalyptus Honig
- Miel de eucalipto
- Thymian Honig
- Miel Tomillo
- KastanienHonig
- Miel de castaño
- Orangenblütenhonig
- Miel azahar
Rosmarin Honig
- Miel Romero
AvocadoHonig
- Miel de Aguacate
Blütenpollen
- Bee Pollen - siehe Beispiel - Fotos
Das ist für den Mix:
Orangenblütenhonig
mit Blüten-Pollen, Gelée Royal &Propolis
Siehe Foto
Der Avocado Honig ist sehr sehr dunkel
Wenn Folie dann so das es sehr betont wird wie bei Vexa-Rino
Wenn Blüten verwendet wird denkt daran
Es sind Die Blüten von wo die Honigsorten - Geschmack entsteht
Rückseite
Abfülldatum /verfalldatum
Wird mit einer stanze drauf gemacht
Freilassen
Herkunft und Anschrift
✅100% Purer Andalusischer Honig
✅Garantiert ohne chemie
✅Abfüllung& Verpackung bei niedrigen Temperaturen & erhaltene Nährstoffe
✅ungefiltert
✅Winter nicht zugefüttert
Honig gilt als Rohkost und ist daher für Kleinkinder unter 12 Monate ungeeignet
Naturbelassener Honig kann im Laufe der Zeit kristallisieren und bei max. 40° C im Wasserbad wieder verflüssigt werden.
Wir hatten an einer no Label Ettiket gedacht
Bedeutet durchsichtige Folie
Siegelverschluss müsste dann an der Seite sein in Papierform
Die LOSnummer und ablaufdatum da drauf gestanzt werden
Könnt es bei Klebwerk.de ansehen
Und Anhang Fotos
Oder auch Baumwolle Papier da kann es i..

```html
<!DOCTYPE html>
<html lang="de">
<head>
<meta charset="utf-8">
<title>TERAMILO Honig – Etiketten</title>
<link rel="stylesheet" href="https://fonts.googleapis.com/css2?family=Josefin+Sans:wght@400;600;700&family=Roboto+Slab:wght@700;900&display=swap">
<style>
:root{
  --bg:#f1f1f1;
  --ink:#1e1e1e;
  --strip:#2b2b2b;
  --honey-light:#f5a21a;
  --honey:#e2660b;
  --honey-deep:#c9520a;
  --avocado-light:#8a3412;
  --avocado:#5e1c08;
  --label-text:#fff4dc;
  --gold:#e9c46a;
  --cream:#fff6e0;
  --brown:#6b2a05;
}
*{box-sizing:border-box;margin:0;padding:0}
html,body{width:1200px;height:4056px;overflow:hidden;background:var(--bg)}
body{position:relative;font-family:"Josefin Sans",sans-serif;color:var(--label-text)}
.row{position:absolute;left:0;width:1200px;height:555px}
.label{position:absolute;top:410px;width:274px;height:258px;background:linear-gradient(180deg,var(--honey-light),var(--honey) 60%,var(--honey-deep));overflow:hidden}
.row.avocado .label{background:linear-gradient(180deg,var(--avocado-light),var(--avocado))}
.back-info{left:167px;padding:78px 20px 0 40px}
.front{left:469px;text-align:center}
.quality{left:770px;padding:62px 20px 0 36px}

.back-info h2,.quality h2{font-family:"Roboto Slab",serif;font-weight:700;font-size:10.5px;letter-spacing:.4px;margin-bottom:3px}
.row.avocado .back-info h2,.row.avocado .quality h2{color:var(--gold)}
.back-info p{font-size:6px;font-weight:600;line-height:1.35;margin-bottom:6px;text-transform:uppercase}
.content{font-size:6px;font-weight:700;margin-top:6px}
.content b{font-family:"Roboto Slab",serif;font-size:17px;font-weight:900;margin-left:4px}

.strip{position:absolute;left:577px;top:300px;width:46px;height:178px;background:var(--strip);z-index:2;display:flex;align-items:flex-end;justify-content:center;padding-bottom:18px}
.strip span{writing-mode:vertical-rl;transform:rotate(180deg);font-size:8px;font-weight:700;letter-spacing:1.6px;color:#fff}
.seal{position:absolute;left:502px;top:138px;width:196px;height:196px;z-index:3;border-radius:50%;background:#fff;border:3px solid var(--ink);display:flex;align-items:center;justify-content:center}
.seal span{font-size:17px;font-weight:700;letter-spacing:3px;color:var(--ink)}

.front .claim{position:absolute;top:100px;left:0;right:0;font-size:8.5px;font-weight:700;color:#fff}
.front .wings{position:absolute;top:92px;left:24px;width:226px;height:100px;background:linear-gradient(90deg,var(--wing),rgba(255,255,255,.25) 30%,transparent 50%,rgba(255,255,255,.25) 70%,var(--wing));opacity:.9;clip-path:polygon(0 20%,40% 0,50% 30%,60% 0,100% 20%,88% 80%,55% 100%,45% 100%,12% 80%)}
.front .name{position:absolute;top:122px;left:0;right:0;font-family:"Roboto Slab",serif;font-weight:900;font-size:26px;line-height:.95;color:#fff;text-transform:uppercase}
.front .name.long{font-size:19px}
.front .spanish{position:absolute;top:204px;left:0;right:0;font-size:7.5px;font-weight:700;color:#fff;text-transform:uppercase}

.checks{list-style:none;margin-top:8px}
.checks li{font-size:5.6px;font-weight:700;line-height:1.2;margin-bottom:5px;padding-left:12px;position:relative;text-transform:uppercase;max-width:150px}
.checks li svg{position:absolute;left:0;top:-1px;width:8px;height:8px}
.brand{display:flex;align-items:center;gap:6px;margin-top:6px}
.brand i{width:24px;height:24px;border-radius:50%;border:1.5px solid var(--brown);flex:none}
.row.avocado .brand i{border-color:var(--gold)}
.brand strong{display:block;font-size:8px;letter-spacing:1.5px;color:var(--brown)}
.row.avocado .brand strong{color:var(--gold)}
.brand small{display:block;font-size:4.6px;font-weight:600;line-height:1.25;color:var(--brown)}
.row.avocado .brand small{color:var(--gold)}
.lot{position:absolute;right:18px;top:60px;width:36px;height:140px;background:var(--cream);display:flex;align-items:flex-end;justify-content:center;padding-bottom:8px}
.lot span{writing-mode:vertical-rl;transform:rotate(180deg);font-size:4.6px;font-weight:700;color:var(--brown);letter-spacing:.3px}
</style>
</head>
<body>
<svg width="0" height="0" style="position:absolute">
  <defs>
    <symbol id="tick" viewBox="0 0 10 10">
      <circle cx="5" cy="5" r="4.3" fill="none" stroke="currentColor" stroke-width="1"/>
      <path d="M2.8 5.2l1.6 1.6 3-3.4" fill="none" stroke="currentColor" stroke-width="1.2"/>
    </symbol>
  </defs>
</svg>

<section class="row" style="top:0;--wing:#d9d9d9">
  <div class="seal"><span>TERAMILO</span></div>
  <div class="strip"><span>MIEL ARTISAN</span></div>
  <article class="label back-info">
    <h2>BERG HONIG</h2>
    <p>Dieser Honig aus den Bergen Andalusiens besticht durch sein einzigartiges Aroma und seine Cremigkeit</p>
    <p>Naturbelassener Honig kann im Laufe der Zeit kristallisieren und bei max. 40°C im Wasserbad wieder verflüssigt werden.</p>
    <p>Trocken und vor Wärme geschützt lagern</p>
    <p>Für Kinder unter 12 Monaten nicht geeignet</p>
    <p>Ursprungsland Spanien</p>
    <div class="content">INHALT <b>℮300g</b></div>
  </article>
  <article class="label front">
    <div class="wings" role="img" aria-label="Geometrische Bienenillustration"></div>
    <div class="claim">100% PURES ANDALUSIEN</div>
    <div class="name">Berg<br>Honig</div>
    <div class="spanish">Miel de Monte</div>
  </article>
  <article class="label quality">
    <h2>TERAMILO QUALITÄT</h2>
    <ul class="checks">
      <li><svg><use href="#tick"/></svg>100% purer andalusischer Honig</li>
      <li><svg><use href="#tick"/></svg>Garantiert ohne Chemie</li>
      <li><svg><use href="#tick"/></svg>Ungefiltert und naturbelassen</li>
      <li><svg><use href="#tick"/></svg>Ohne Zufütterung im Winter</li>
      <li><svg><use href="#tick"/></svg>Abfüllung &amp; Verpackung bei niedrigen Temperaturen</li>
    </ul>
    <div class="brand"><i></i><div><strong>TERAMILO</strong><small>CALLE DEL PANAL S/N<br>VALLE DORADO · SPANIEN</small></div></div>
    <div class="lot"><span>LOSNUMMER: &nbsp; MINDESTENS HALTBAR BIS:</span></div>
  </article>
</section>

<section class="row" style="top:555px;--wing:#f7b23b">
  <div class="seal"><span>TERAMILO</span></div>
  <div class="strip"><span>MIEL ARTISAN</span></div>
  <article class="label back-info">
    <h2>ORANGENBLÜTEN HONIG</h2>
    <p>Dieser Honig aus Orangenblüten besticht durch sein einzigartiges Aroma und seine Cremigkeit</p>
    <p>Naturbelassener Honig kann im Laufe der Zeit kristallisieren und bei max. 40°C im Wasserbad wieder verflüssigt werden.</p>
    <p>Trocken und vor Wärme geschützt lagern</p>
    <p>Für Kinder unter 12 Monaten nicht geeignet</p>
    <p>Ursprungsland Spanien</p>
    <div class="content">INHALT <b>℮300g</b></div>
  </article>
  <article class="label front">
    <div class="wings" role="img" aria-label="Geometrische Bienenillustration"></div>
    <div class="claim">100% PURES ANDALUSIEN</div>
    <div class="name long">Orangenblüten<br>Honig</div>
    <div class="spanish">Miel de Azahar</div>
  </article>
  <article class="label quality">
    <h2>TERAMILO QUALITÄT</h2>
    <ul class="checks">
      <li><svg><use href="#tick"/></svg>100% purer andalusischer Honig</li>
      <li><svg><use href="#tick"/></svg>Garantiert ohne Chemie</li>
      <li><svg><use href="#tick"/></svg>Ungefiltert und naturbelassen</li>
      <li><svg><use href="#tick"/></svg>Ohne Zufütterung im Winter</li>
      <li><svg><use href="#tick"/></svg>Abfüllung &amp; Verpackung bei niedrigen Temperaturen</li>
    </ul>
    <div class="brand"><i></i><div><strong>TERAMILO</strong><small>CALLE DEL PANAL S/N<br>VALLE DORADO · SPANIEN</small></div></div>
    <div class="lot"><span>LOSNUMMER: &nbsp; MINDESTENS HALTBAR BIS:</span></div>
  </article>
</section>

<section class="row avocado" style="top:1110px;--wing:#e9c46a">
  <div class="seal"><span>TERAMILO</span></div>
  <div class="strip"><span>MIEL ARTISAN</span></div>
  <article class="label back-info">
    <h2>AVOCADO HONIG</h2>
    <p>Dieser Honig aus Avocadoblüten besticht durch sein einzigartiges Aroma und seine Cremigkeit</p>
    <p>Naturbelassener Honig kann im Laufe der Zeit kristallisieren und bei max. 40°C im Wasserbad wieder verflüssigt werden.</p>
    <p>Trocken und vor Wärme geschützt lagern</p>
    <p>Für Kinder unter 12 Monaten nicht geeignet</p>
    <p>Ursprungsland Spanien</p>
    <div class="content">INHALT <b>℮300g</b></div>
  </article>
  <article class="label front">
    <div class="wings" role="img" aria-label="Geometrische Bienenillustration"></div>
    <div class="claim">100% PURES ANDALUSIEN</div>
    <div class="name" style="color:var(--gold)">Avocado<br>Honig</div>
    <div class="spanish">Miel de Aguacate</div>
  </article>
  <article class="label quality">
    <h2>TERAMILO QUALITÄT</h2>
    <ul class="checks">
      <li><svg><use href="#tick"/></svg>100% purer andalusischer Honig</li>
      <li><svg><use href="#tick"/></svg>Garantiert ohne Chemie</li>
      <li><svg><use href="#tick"/></svg>Ungefiltert und naturbelassen</li>
      <li><svg><use href="#tick"/></svg>Ohne Zufütterung im Winter</li>
      <li><svg><use href="#tick"/></svg>Abfüllung &amp; Verpackung bei niedrigen Temperaturen</li>
    </ul>
    <div class="brand"><i></i><div><strong>TERAMILO</strong><small>CALLE DEL PANAL S/N<br>VALLE DORADO · SPANIEN</small></div></div>
    <div class="lot"><span>LOSNUMMER: &nbsp; MINDESTENS HALTBAR BIS:</span></div>
  </article>
</section>

<section class="row" style="top:1665px;--wing:#7fd1c7">
  <div class="seal"><span>TERAMILO</span></div>
  <div class="strip"><span>MIEL ARTISAN</span></div>
  <article class="label back-info">
    <h2>EUKALYPTUS HONIG</h2>
    <p>Dieser Honig aus Eukalyptusblüten besticht durch sein einzigartiges Aroma und seine Cremigkeit</p>
    <p>Naturbelassener Honig kann im Laufe der Zeit kristallisieren und bei max. 40°C im Wasserbad wieder verflüssigt werden.</p>
    <p>Trocken und vor Wärme geschützt lagern</p>
    <p>Für Kinder unter 12 Monaten nicht geeignet</p>
    <p>Ursprungsland Spanien</p>
    <div class="content">INHALT <b>℮300g</b></div>
  </article>
  <article class="label front">
    <div class="wings" role="img" aria-label="Geometrische Bienenillustration"></div>
    <div class="claim">100% PURES ANDALUSIEN</div>
    <div class="name long">Eukalyptus<br>Honig</div>
    <div class="spanish">Miel de Eucalipto</div>
  </article>
  <article class="label quality">
    <h2>TERAMILO QUALITÄT</h2>
    <ul class="checks">
      <li><svg><use href="#tick"/></svg>100% purer andalusischer Honig</li>
      <li><svg><use href="#tick"/></svg>Garantiert ohne Chemie</li>
      <li><svg><use href="#tick"/></svg>Ungefiltert und naturbelassen</li>
      <li><svg><use href="#tick"/></svg>Ohne Zufütterung im Winter</li>
      <li><svg><use href="#tick"/></svg>Abfüllung &amp; Verpackung bei niedrigen Temperaturen</li>
    </ul>
    <div class="brand"><i></i><div><strong>TERAMILO</strong><small>CALLE DEL PANAL S/N<br>VALLE DORADO · SPANIEN</small></div></div>
    <div class="lot"><span>LOSNUMMER: &nbsp; MINDESTENS HALTBAR BIS:</span></div>
  </article>
</section>

<section class="row" style="top:2220px;--wing:#b7a3e0">
  <div class="seal"><span>TERAMILO</span></div>
  <div class="strip"><span>MIEL ARTISAN</span></div>
  <article class="label back-info">
    <h2>THYMIAN HONIG</h2>
    <p>Dieser Honig aus Thymianblüten besticht durch sein einzigartiges Aroma und seine Cremigkeit</p>
    <p>Naturbelassener Honig kann im Laufe der Zeit kristallisieren und bei max. 40°C im Wasserbad wieder verflüssigt werden.</p>
    <p>Trocken und vor Wärme geschützt lagern</p>
    <p>Für Kinder unter 12 Monaten nicht geeignet</p>
    <p>Ursprungsland Spanien</p>
    <div class="content">INHALT <b>℮300g</b></div>
  </article>
  <article class="label front">
    <div class="wings" role="img" aria-label="Geometrische Bienenillustration"></div>
    <div class="claim">100% PURES ANDALUSIEN</div>
    <div class="name">Thymian<br>Honig</div>
    <div class="spanish">Miel de Tomillo</div>
  </article>
  <article class="label quality">
    <h2>TERAMILO QUALITÄT</h2>
    <ul class="checks">
      <li><svg><use href="#tick"/></svg>100% purer andalusischer Honig</li>
      <li><svg><use href="#tick"/></svg>Garantiert ohne Chemie</li>
      <li><svg><use href="#tick"/></svg>Ungefiltert und naturbelassen</li>
      <li><svg><use href="#tick"/></svg>Ohne Zufütterung im Winter</li>
      <li><svg><use href="#tick"/></svg>Abfüllung &amp; Verpackung bei niedrigen Temperaturen</li>
    </ul>
    <div class="brand"><i></i><div><strong>TERAMILO</strong><small>CALLE DEL PANAL S/N<br>VALLE DORADO · SPANIEN</small></div></div>
    <div class="lot"><span>LOSNUMMER: &nbsp; MINDESTENS HALTBAR BIS:</span></div>
  </article>
</section>

<section class="row" style="top:2775px;--wing:#f2a0b8">
  <div class="seal"><span>TERAMILO</span></div>
  <div class="strip"><span>MIEL ARTISAN</span></div>
  <article class="label back-info">
    <h2>KASTANIEN HONIG</h2>
    <p>Dieser Honig aus Kastanienblüten besticht durch sein einzigartiges Aroma und seine Cremigkeit</p>
    <p>Naturbelassener Honig kann im Laufe der Zeit kristallisieren und bei max. 40°C im Wasserbad wieder verflüssigt werden.</p>
    <p>Trocken und vor Wärme geschützt lagern</p>
    <p>Für Kinder unter 12 Monaten nicht geeignet</p>
    <p>Ursprungsland Spanien</p>
    <div class="content">INHALT <b>℮300g</b></div>
  </article>
  <article class="label front">
    <div class="wings" role="img" aria-label="Geometrische Bienenillustration"></div>
    <div class="claim">100% PURES ANDALUSIEN</div>
    <div class="name long">Kastanien<br>Honig</div>
    <div class="spanish">Miel de Castaño</div>
  </article>
  <article class="label quality">
    <h2>TERAMILO QUALITÄT</h2>
    <ul class="checks">
      <li><svg><use href="#tick"/></svg>100% purer andalusischer Honig</li>
      <li><svg><use href="#tick"/></svg>Garantiert ohne Chemie</li>
      <li><svg><use href="#tick"/></svg>Ungefiltert und naturbelassen</li>
      <li><svg><use href="#tick"/></svg>Ohne Zufütterung im Winter</li>
      <li><svg><use href="#tick"/></svg>Abfüllung &amp; Verpackung bei niedrigen Temperaturen</li>
    </ul>
    <div class="brand"><i></i><div><strong>TERAMILO</strong><small>CALLE DEL PANAL S/N<br>VALLE DORADO · SPANIEN</small></div></div>
    <div class="lot"><span>LOSNUMMER: &nbsp; MINDESTENS HALTBAR BIS:</span></div>
  </article>
</section>

<section class="row" style="top:3330px;--wing:#8fb0e8">
  <div class="seal"><span>TERAMILO</span></div>
  <div class="strip"><span>MIEL ARTISAN</span></div>
  <article class="label back-info">
    <h2>ROSMARIN HONIG</h2>
    <p>Dieser Honig aus Rosmarinblüten besticht durch sein einzigartiges Aroma und seine Cremigkeit</p>
    <p>Naturbelassener Honig kann im Laufe der Zeit kristallisieren und bei max. 40°C im Wasserbad wieder verflüssigt werden.</p>
    <p>Trocken und vor Wärme geschützt lagern</p>
    <p>Für Kinder unter 12 Monaten nicht geeignet</p>
    <p>Ursprungsland Spanien</p>
    <div class="content">INHALT <b>℮300g</b></div>
  </article>
  <article class="label front">
    <div class="wings" role="img" aria-label="Geometrische Bienenillustration"></div>
    <div class="claim">100% PURES ANDALUSIEN</div>
    <div class="name">Rosmarin<br>Honig</div>
    <div class="spanish">Miel de Romero</div>
  </article>
  <article class="label quality">
    <h2>TERAMILO QUALITÄT</h2>
    <ul class="checks">
      <li><svg><use href="#tick"/></svg>100% purer andalusischer Honig</li>
      <li><svg><use href="#tick"/></svg>Garantiert ohne Chemie</li>
      <li><svg><use href="#tick"/></svg>Ungefiltert und naturbelassen</li>
      <li><svg><use href="#tick"/></svg>Ohne Zufütterung im Winter</li>
      <li><svg><use href="#tick"/></svg>Abfüllung &amp; Verpackung bei niedrigen Temperaturen</li>
    </ul>
    <div class="brand"><i></i><div><strong>TERAMILO</strong><small>CALLE DEL PANAL S/N<br>VALLE DORADO · SPANIEN</small></div></div>
    <div class="lot"><span>LOSNUMMER: &nbsp; MINDESTENS HALTBAR BIS:</span></div>
  </article>
</section>
</body>
</html>
```